Bitcoin Casino User Interface

This is a responsive design for a new bitcoin casino called the brass latch casino

The 4 games I need the Ui for are video poker, blackjack, roulette and dice

The designs should be ideal for mobile and have a bit of a retro feel

Good example is www.plumreelhallvexcom

Target Market(s)

Adults between the ages of 21-55 all over the world

Industry/Entity Type

Casino

Font styles to use
Serif

Colors
5dc4b5
ffffff

Requirements
Must have
• Must be responsive and look great on mobile
design must be functional
Should not have
• Any generic and standard elements

```html
<!DOCTYPE html>
<html lang="en">
<head>
<meta charset="utf-8">
<title>Brass Latch Casino App v1 – Video Poker</title>
<link rel="stylesheet" href="https://fonts.googleapis.com/css2?family=Rokkitt:wght@400;500&family=Roboto:wght@300;400;700&family=Lobster&display=swap">
<style>
:root{
  --page:#ffffff;
  --ink:#111111;
  --teal:#63c4b3;
  --teal-light:#83d3c6;
  --red:#ff3a3a;
  --blue:#1a82fb;
  --orange:#ff9b1f;
  --grey-btn:#8f8f8f;
  --green:#4cd964;
  --black:#111111;
  --felt:#b4b4b4;
  --card:#ffffff;
  --card-back:#1a82fb;
  --hold:#5aa9f5;
}
*{box-sizing:border-box;margin:0;padding:0}
html,body{width:1200px;height:693px;overflow:hidden;background:var(--page)}
body{position:relative;font-family:"Roboto",Arial,sans-serif;color:var(--ink)}

.board-title{position:absolute;left:17px;top:7px;font-size:11px;line-height:13px}
.board-title strong{font-weight:700}
.screen-label{position:absolute;top:668px;width:557px;text-align:center;font-size:15px}

.screen{position:absolute;top:202px;width:557px;height:313px;box-shadow:0 0 3px rgba(0,0,0,.35)}
.screen--deal{left:30px}
.screen--draw{left:630px}

/* status bar */
.status{position:absolute;left:0;top:0;width:557px;height:46px;display:flex}
.status__cell{height:46px;padding:9px 0 0;text-align:center;color:#fff}
.status__cell small{display:block;font-size:8px;font-style:italic;font-weight:300}
.status__cell b{display:block;font-size:9px;font-weight:700;margin-top:4px}
.status__credits{width:70px;background:var(--black)}
.status__bet{width:70px;background:var(--red)}
.status__result{width:277px;background:#fff;color:var(--ink);position:relative;text-align:left}
.status__result .field{position:absolute;top:9px}
.status__result small{font-size:8px}
.status__result b{font-size:9px;font-weight:400;margin-top:4px}
.verify{position:absolute;left:214px;top:6px;width:57px;height:34px;background:var(--green);color:#fff;font-size:12px;font-weight:300;display:flex;align-items:center;justify-content:center}
.status__help{width:70px;background:var(--blue);font-size:12px;font-weight:300;padding-top:16px}
.status__home{width:70px;background:var(--black);display:flex;align-items:center;justify-content:center;padding:0}

/* pay table */
.paytable{position:absolute;left:0;top:46px;width:487px;height:177px;display:grid;grid-template-columns:140px 69px 69px 70px 69px 70px;grid-template-rows:repeat(9,1fr);font-family:"Rokkitt",Georgia,serif;font-size:13px}
.paytable span{display:flex;align-items:center;justify-content:center;color:#fff}
.paytable .hand{justify-content:flex-start;padding-left:7px;background:var(--teal);color:#12302b;font-weight:500;font-size:14px}
.paytable .c1{background:var(--red)}
.paytable .c2,.paytable .c4{background:var(--teal-light);color:#23463f}
.paytable .c3,.paytable .c5{background:var(--teal);color:#23463f}

/* action buttons */
.actions{position:absolute;left:487px;top:46px;width:70px;height:267px;display:flex;flex-direction:column}
.actions span{flex:1;display:flex;align-items:center;justify-content:center;color:#fff;font-size:12px;font-weight:300;border-bottom:1px solid rgba(255,255,255,.35)}
.btn-auto{background:var(--orange)}
.btn-split{background:var(--grey-btn);color:#cfcfcf!important}
.btn-blue{background:var(--blue)}
.btn-main{background:var(--red);font-family:"Lobster",Georgia,serif;font-size:19px!important;font-weight:400!important;border:0!important}

/* table felt with cards */
.felt{position:absolute;left:0;top:223px;width:487px;height:90px;background:var(--felt)}
.card{position:absolute;top:5px;width:60px;height:80px;background:var(--card);border-radius:3px;box-shadow:0 2px 0 rgba(0,0,0,.25)}
.card--back::after{content:"";position:absolute;left:5px;top:5px;right:5px;bottom:10px;background:var(--card-back);border-radius:2px}
.card__rank{position:absolute;left:6px;top:2px;font-family:"Roboto",Arial,sans-serif;font-size:15px;line-height:16px}
.card__pip{position:absolute;left:5px;top:18px;font-size:14px;line-height:14px}
.card__suit{position:absolute;left:0;right:0;bottom:4px;text-align:center;font-size:30px;line-height:30px}
.red{color:var(--red)}
.black{color:var(--ink)}
.hold{position:absolute;left:0;right:0;top:28px;height:22px;background:var(--hold);color:#fff;font-family:"Roboto",Arial,sans-serif;font-weight:700;font-size:16px;text-align:center;line-height:22px}
</style>
</head>
<body>

<p class="board-title"><strong>Brass Latch Casino App v1:</strong> iOS<br>(September 2014)</p>

<!-- Deal state -->
<section class="screen screen--deal">
  <div class="status">
    <div class="status__cell status__credits"><small>Credits:</small><b>00000</b></div>
    <div class="status__cell status__bet"><small>Bet:</small><b>00000</b></div>
    <div class="status__cell status__result">
      <div class="field" style="left:9px"><small>Result:</small><b>Lorem Ipsum Dolors Sit Amet</b></div>
      <div class="field" style="left:147px"><small>BTC Payout:</small><b>0000000000</b></div>
      <span class="verify">Verify</span>
    </div>
    <div class="status__cell status__help">Help</div>
    <div class="status__cell status__home"><svg width="20" height="18" viewBox="0 0 20 18" fill="none" stroke="#fff" stroke-width="1.4"><path d="M1 9 10 1l9 8M4 7v10h4v-6h4v6h4V7"/></svg></div>
  </div>
  <div class="paytable">
    <span class="hand">Royal Flush</span><span class="c1">250</span><span class="c2">500</span><span class="c3">750</span><span class="c4">1000</span><span class="c5">4337.80</span>
    <span class="hand">Straight Flush</span><span class="c1">50</span><span class="c2">100</span><span class="c3">150</span><span class="c4">200</span><span class="c5">250</span>
    <span class="hand">4 of a Kind</span><span class="c1">25</span><span class="c2">50</span><span class="c3">75</span><span class="c4">100</span><span class="c5">125</span>
    <span class="hand">Full House</span><span class="c1">9</span><span class="c2">18</span><span class="c3">27</span><span class="c4">36</span><span class="c5">45</span>
    <span class="hand">Flush</span><span class="c1">6</span><span class="c2">12</span><span class="c3">18</span><span class="c4">24</span><span class="c5">30</span>
    <span class="hand">Straight</span><span class="c1">4</span><span class="c2">8</span><span class="c3">12</span><span class="c4">16</span><span class="c5">20</span>
    <span class="hand">3 of a Kind</span><span class="c1">3</span><span class="c2">6</span><span class="c3">9</span><span class="c4">12</span><span class="c5">15</span>
    <span class="hand">Two Pair</span><span class="c1">2</span><span class="c2">4</span><span class="c3">6</span><span class="c4">8</span><span class="c5">10</span>
    <span class="hand">Jacks or Better</span><span class="c1">1</span><span class="c2">2</span><span class="c3">3</span><span class="c4">4</span><span class="c5">5</span>
  </div>
  <div class="actions">
    <span class="btn-auto">Auto</span><span class="btn-split">Split</span><span class="btn-blue">Double</span><span class="btn-blue">Stand</span><span class="btn-blue">Hit</span><span class="btn-main">Deal</span>
  </div>
  <div class="felt">
    <div class="card card--back" style="left:75px"></div>
    <div class="card card--back" style="left:145px"></div>
    <div class="card card--back" style="left:215px"></div>
    <div class="card card--back" style="left:285px"></div>
    <div class="card card--back" style="left:355px"></div>
  </div>
</section>

<!-- Draw state -->
<section class="screen screen--draw">
  <div class="status">
    <div class="status__cell status__credits"><small>Credits:</small><b>00000</b></div>
    <div class="status__cell status__bet"><small>Bet:</small><b>00000</b></div>
    <div class="status__cell status__result">
      <div class="field" style="left:9px"><small>Result:</small><b>Lorem Ipsum Dolors Sit Amet</b></div>
      <div class="field" style="left:147px"><small>BTC Payout:</small><b>0000000000</b></div>
      <span class="verify">Verify</span>
    </div>
    <div class="status__cell status__help">Help</div>
    <div class="status__cell status__home"><svg width="20" height="18" viewBox="0 0 20 18" fill="none" stroke="#fff" stroke-width="1.4"><path d="M1 9 10 1l9 8M4 7v10h4v-6h4v6h4V7"/></svg></div>
  </div>
  <div class="paytable">
    <span class="hand">Royal Flush</span><span class="c1">250</span><span class="c2">500</span><span class="c3">750</span><span class="c4">1000</span><span class="c5">4337.80</span>
    <span class="hand">Straight Flush</span><span class="c1">50</span><span class="c2">100</span><span class="c3">150</span><span class="c4">200</span><span class="c5">250</span>
    <span class="hand">4 of a Kind</span><span class="c1">25</span><span class="c2">50</span><span class="c3">75</span><span class="c4">100</span><span class="c5">125</span>
    <span class="hand">Full House</span><span class="c1">9</span><span class="c2">18</span><span class="c3">27</span><span class="c4">36</span><span class="c5">45</span>
    <span class="hand">Flush</span><span class="c1">6</span><span class="c2">12</span><span class="c3">18</span><span class="c4">24</span><span class="c5">30</span>
    <span class="hand">Straight</span><span class="c1">4</span><span class="c2">8</span><span class="c3">12</span><span class="c4">16</span><span class="c5">20</span>
    <span class="hand">3 of a Kind</span><span class="c1">3</span><span class="c2">6</span><span class="c3">9</span><span class="c4">12</span><span class="c5">15</span>
    <span class="hand">Two Pair</span><span class="c1">2</span><span class="c2">4</span><span class="c3">6</span><span class="c4">8</span><span class="c5">10</span>
    <span class="hand">Jacks or Better</span><span class="c1">1</span><span class="c2">2</span><span class="c3">3</span><span class="c4">4</span><span class="c5">5</span>
  </div>
  <div class="actions">
    <span class="btn-auto">Auto</span><span class="btn-split">Split</span><span class="btn-blue">Double</span><span class="btn-blue">Stand</span><span class="btn-blue">Hit</span><span class="btn-main">Draw</span>
  </div>
  <div class="felt">
    <div class="card" style="left:75px"><span class="card__rank red">J</span><span class="card__pip red">♦</span><span class="card__suit red">♦</span><span class="hold">HOLD</span></div>
    <div class="card" style="left:145px"><span class="card__rank black">Q</span><span class="card__pip black">♠</span><span class="card__suit black">♠</span><span class="hold">HOLD</span></div>
    <div class="card" style="left:215px"><span class="card__rank black">K</span><span class="card__pip black">♣</span><span class="card__suit black">♣</span></div>
    <div class="card" style="left:285px"><span class="card__rank red">A</span><span class="card__pip red">♥</span><span class="card__suit red">♥</span></div>
    <div class="card" style="left:355px"><span class="card__rank red">10</span><span class="card__pip red">♥</span><span class="card__suit red">♥</span></div>
  </div>
</section>

<p class="screen-label" style="left:30px">Video Poker</p>
<p class="screen-label" style="left:630px">Video Poker</p>

</body>
</html>
```